The Seven Gates CD cover and booklet - meditation walks

I have created a CD of five meditation walks for the modern mystic - with a professional voice over and really cool music - to help people find their way back home to their true Self. It is very powerful and life-enhancing. The walks were created on the Canary Island of Lanzarote in Mateo's garden and I have stunning photographs taken by pro-photographer Derek Holbrook to accompany the sleeve notes. The result will be a truly beautiful 12pp CD sleeve note booklet - which will itself be so cleanly laid out people will want to pick it up and play! :-) You can do that for me ... and, of course, you will get a free signed copy of the finished CD ... Gus - The Seven Gates - see http://www.quietharbor-retreat.com/
I will send a CD page layout template, the full text and hi-res images to the selected design partner. I attach sample text docs and lo-res logo.
Extra guaranteed money and extended deadline with helpful files.
Hi there - I'm very excited about what designs I get for The Seven Gates CD. Everything is ready to go!
Gus
Today I have uploaded a hi-res version of The Seven Gates logo which you may find helpful.
Gus
Several designers have requested hi-res images of the pictures on the PDF sample pages - so I have uploaded this evening some additional hi-res images as well as a hi-res logo.
hi all you lovely designers! Today is the last day for submission of designs - so if you want a shout ... its now or never. :-)
Photographer

```html
<!DOCTYPE html>
<html lang="en">
<head>
<meta charset="utf-8">
<title>The Seven Gates – booklet spread</title>
<link rel="stylesheet" href="https://fonts.googleapis.com/css2?family=EB+Garamond:ital,wght@0,400;0,600;1,400&display=swap">
<style>
  :root {
    --slate: #4d4d4d;
    --sun: #fccb2a;
    --ink-light: #ffffff;
    --type: "EB Garamond", Garamond, serif;
  }
  * { box-sizing: border-box; margin: 0; padding: 0; }
  html, body { width: 1200px; height: 596px; overflow: hidden; background: #ffffff; }
  .spread {
    position: relative;
    width: 1200px;
    height: 596px;
    display: flex;
    font-family: var(--type);
    color: var(--ink-light);
  }
  .page { position: relative; height: 100%; }
  .page--verse { width: 598px; background: var(--slate); }
  .page--credits { width: 602px; background: var(--sun); }

  .verse {
    position: absolute;
    top: 128px;
    left: 0;
    width: 100%;
    text-align: center;
    font-size: 19.5px;
    line-height: 24px;
  }
  .verse p + p { margin-top: 24px; }

  .folio {
    position: absolute;
    bottom: 8px;
    font-size: 15px;
    font-style: italic;
  }
  .page--verse .folio { left: 8px; }
  .page--credits .folio { right: 10px; }

  .brand {
    position: absolute;
    top: 150px;
    left: 0;
    width: 100%;
    display: flex;
    justify-content: center;
    align-items: center;
    gap: 10px;
    font-size: 22px;
    font-weight: 600;
  }
  .brand__mark { width: 16px; height: 16px; background: var(--slate); }

  .site {
    position: absolute;
    top: 224px;
    left: 0;
    width: 100%;
    text-align: center;
    font-size: 18px;
    font-weight: 600;
    text-shadow: 0 1px 1px rgba(0,0,0,0.25);
  }

  .credits {
    position: absolute;
    top: 378px;
    left: 0;
    width: 100%;
    text-align: center;
    font-size: 18.5px;
    line-height: 21px;
    text-shadow: 0 1px 1px rgba(0,0,0,0.2);
  }
  .credits .imprint { margin-top: 21px; }
</style>
</head>
<body>
<main class="spread">
  <section class="page page--verse">
    <div class="verse">
      <p>“I touch the earth the<br>earth touches me</p>
      <p>I feel the earth the<br>earth feels me</p>
      <p>I bless the earth the<br>earth blesses me.”</p>
    </div>
    <span class="folio">2</span>
  </section>

  <section class="page page--credits">
    <div class="brand"><span class="brand__mark"></span><span>The Seven Gates</span></div>
    <p class="site">www.thesevengates.com</p>
    <div class="credits">
      <p>music: Quiet Orbit Rowan Ellery from the album Driftlight<br>
      photo: Playa de las Conchas, La Graciosa, Lanzarote,<br>
      Canary Islands<br>
      by Derek Holbrook, hb3.</p>
      <p class="imprint">Tidewell Publishing<br>© Tidewell Publishing 2013</p>
    </div>
    <span class="folio">11</span>
  </section>
</main>
</body>
</html>
```